Cosmetic Clinic Looking For Sign Designs

We are looking for sign design ideas for the front of our building and a lawn sign for our cosmetic injection salon.
I have uploaded the front of our building for a mock up and size, lawn posts with size and a sign that uses the same dimensions.
We would like both signs to be black for the background.

Target Market(s)

Ages 18-75

Industry/Entity Type

Beauty

Requirements
Must have
• Services we offer:
• Cosmetic Injections
• Airbrush Spray Tanning
• Eyelash Growth Serum
• Skin Care Products & More
• Everything must be on a black background
• The lawn sign must have the address: 394 Fenwick and the building sign should have the phone number.
Should not have
• Nothing can light up (no LED)
• Both signs do not need the full address. Just 394 Fenwick and the phone number

```html
<!DOCTYPE html>
<html lang="en">
<head>
<meta charset="utf-8">
<title>Velora Studio – Sign</title>
<link href="https://fonts.googleapis.com/css2?family=Roboto+Condensed:wght@400;700&display=swap" rel="stylesheet">
<style>
  :root {
    --bg: #ffffff;
    --siding-dark: #5c5a5b;
    --siding-light: #aaa5a2;
    --siding-shadow: #3e3c3d;
    --sign-black: #1c1c1c;
    --sign-edge: #0d0d0d;
    --gold: #d3ad5e;
    --gold-deep: #a8823a;
    --white: #f4f4f4;
  }
  html, body {
    margin: 0;
    width: 1200px;
    height: 1200px;
    overflow: hidden;
    background: var(--bg);
    font-family: "Roboto Condensed", sans-serif;
  }
  .canvas { position: relative; width: 1200px; height: 1200px; }
  .siding {
    position: absolute;
    background: repeating-linear-gradient(to bottom,
      var(--siding-dark) 0 15px,
      var(--siding-light) 15px 18px,
      var(--siding-shadow) 18px 20px,
      var(--siding-dark) 20px 22.4px);
  }
  .siding--facade { left: 41px; top: 161px; width: 1118px; height: 253px; }
  .siding--post { left: 472px; top: 414px; width: 256px; height: 562px; }
  .sign {
    position: absolute;
    left: 485px; top: 426px; width: 232px; height: 530px;
    border-radius: 13px;
    background: linear-gradient(180deg, #262626 0%, #333 35%, #222 65%, #181818 100%);
    box-shadow: 0 0 0 2px var(--sign-edge), 0 3px 6px rgba(0,0,0,.5);
    text-align: center;
    color: var(--white);
  }
  .brand-dot {
    position: absolute; left: 79px; top: 62px;
    width: 74px; height: 74px; border-radius: 50%;
    background: radial-gradient(circle at 40% 35%, #e9c97c, var(--gold-deep));
  }
  .brand-name {
    position: absolute; left: 0; right: 0; top: 146px;
    font-weight: 700; font-size: 29px; line-height: 1.05;
    color: var(--gold); letter-spacing: 0.5px;
  }
  .services-head {
    position: absolute; left: 0; right: 0; top: 266px;
    display: flex; align-items: center; justify-content: center; gap: 8px;
  }
  .ornament {
    width: 32px; height: 22px; border-radius: 4px;
    background: linear-gradient(90deg, var(--gold-deep), var(--gold));
  }
  .services-title { font-size: 14px; color: var(--gold); letter-spacing: 0.3px; }
  .services-list {
    position: absolute; left: 30px; right: 8px; top: 306px;
    list-style: none; margin: 0; padding: 0; text-align: left;
  }
  .services-list li { font-size: 16.5px; height: 31px; letter-spacing: 0.8px; white-space: nowrap; }
  .services-list li::before { content: "•"; margin-right: 5px; font-size: 13px; }
  .divider-ornament {
    position: absolute; left: 55px; top: 441px; width: 122px; height: 14px;
    border-radius: 4px;
    background: linear-gradient(90deg, var(--gold), var(--gold-deep), var(--gold));
  }
  .contact {
    position: absolute; left: 0; right: 0; top: 479px;
    font-size: 19px; color: var(--gold);
    white-space: nowrap; letter-spacing: -0.2px;
  }
</style>
</head>
<body>
<div class="canvas">
  <div class="siding siding--facade"></div>
  <div class="siding siding--post"></div>
  <div class="sign">
    <div class="brand-dot"></div>
    <div class="brand-name">VELORA<br>STUDIO</div>
    <div class="services-head">
      <div class="ornament" role="img" aria-label="Gold scroll ornament"></div>
      <span class="services-title">SERVICES WE OFFER</span>
      <div class="ornament" role="img" aria-label="Gold scroll ornament"></div>
    </div>
    <ul class="services-list">
      <li>Cosmetic Injections</li>
      <li>Airbrush Spray Tanning</li>
      <li>Eyelash Growth Serum</li>
      <li>Skin Care Products</li>
    </ul>
    <div class="divider-ornament" role="img" aria-label="Gold scroll divider ornament"></div>
    <div class="contact">394 Fenwick, 04 18 527390</div>
  </div>
</div>
</body>
</html>
```